A Training Firm needs a Brochure - Steady Course Onboarding Learning Brochure

Quenlith, a HR Consulting Firm focused on Training & Development is seeking a Brochure Design for one of its training programs - Steady Course Onboarding Learning Program.

The designs should be innovative,image led and interesting to read. We would like to see designs that incorporate the colours Blue and Green. Because this company is based in Africa, we would like the designers to use image of Black people instead of Caucasians.

Quenlith is a member of Brightmere Group, a HR Consulting firm that offers services in the area of Learning, Talent Solutions, Outsourcing and Strategy Consulting

Target Market(s)

CEOs, HR Directors, Heads of Learning and Learning Managers of Large, Medium and Small Scale Organisations in Nigeria

Industry/Entity Type

Training

Other font styles liked:
• Corbel

Colors
3176b5
abd036

Requirements
Must have
• Quenlith Logo, A link with the Parent Company Brightmere Group (We usually add that Quenlith is a member of the Brightmere Group) The Group Logo and the Pantone Colours have been attached
Nice to have
• The entire Brochure should be graphically led. That is, lots of graphics - Infographics/Images/colours etc
Should not have
• No Caucasian images. We are an African based Firm and would like to have African images

```html
<!DOCTYPE html>
<html lang="en">
<head>
<meta charset="utf-8">
<title>Steady Course Onboarding Learning Program</title>
<link href="https://fonts.googleapis.com/css2?family=Open+Sans:ital,wght@0,400;0,600;0,700;1,700&display=swap" rel="stylesheet">
<style>
  :root {
    --teal: #12808f;
    --teal-text: #1b7d8c;
    --lime: #b6d07f;
    --body: #6e6e6e;
    --page: #ffffff;
    --logo-blue: #23566e;
  }
  * { margin: 0; padding: 0; box-sizing: border-box; }
  html, body { width: 850px; height: 1200px; overflow: hidden; background: var(--page); }
  body { position: relative; font-family: "Open Sans", Arial, sans-serif; color: var(--body); }

  .title-band {
    position: absolute; left: 0; top: 59px; width: 775px; height: 118px;
    background: var(--teal); color: #fff; padding: 20px 0 0 60px;
  }
  .title-band h1 { font-size: 32px; line-height: 40px; font-weight: 700; }
  .title-band p { font-size: 31px; line-height: 40px; font-weight: 400; }
  .title-accent { position: absolute; left: 775px; top: 59px; width: 60px; height: 118px; background: var(--lime); }

  .office-photo {
    position: absolute; left: 60px; top: 240px; width: 715px; height: 217px;
    background: linear-gradient(180deg, #cfd6da 0%, #e6eaec 45%, #b9c0c4 75%, #4a4d50 100%);
  }

  .solution-heading {
    position: absolute; left: 60px; top: 508px; font-size: 21px; font-weight: 700; color: var(--teal-text);
  }
  .solution-intro {
    position: absolute; left: 60px; top: 563px; width: 750px;
    font-size: 14.6px; line-height: 19.5px; letter-spacing: -0.1px;
  }

  .course-icon { position: absolute; left: 60px; top: 678px; width: 60px; height: 60px; background: var(--teal); }
  .course-label {
    position: absolute; left: 149px; top: 674px; width: 170px;
    font-size: 16px; line-height: 20px; font-weight: 700; color: var(--teal-text);
  }
  .course-text {
    position: absolute; left: 346px; top: 674px; width: 450px;
    font-size: 12.4px; line-height: 15.6px; letter-spacing: -0.1px;
  }
  .course-text p { margin-bottom: 15px; }
  .course-text em { font-weight: 700; }

  .brand { position: absolute; left: 60px; top: 1128px; display: flex; align-items: center; gap: 10px; }
  .brand-name { font-size: 30px; font-weight: 700; color: var(--logo-blue); letter-spacing: -0.5px; }
  .brand-mark { width: 22px; height: 22px; background: var(--lime); }
  .brand-parent { position: absolute; left: 150px; top: 1167px; font-size: 8px; color: var(--body); }

  .page-number {
    position: absolute; left: 775px; top: 1121px; width: 60px; height: 59px; background: var(--lime);
    color: #fff; font-size: 29px; display: flex; align-items: center; justify-content: center;
  }
</style>
</head>
<body>
  <header class="title-band">
    <h1>Steady Course Onboarding</h1>
    <p>Learning Program</p>
  </header>
  <div class="title-accent"></div>

  <div class="office-photo" role="img" aria-label="Bright modern open-plan office with desks, chairs and glass partitions"></div>

  <h2 class="solution-heading">Our Steady Course Onboarding Solution</h2>
  <p class="solution-intro">Based on extensive research we carried out regarding factors that predict the success of a newly hired employee, involving over 200 HR professionals and Line Managers, we discovered that certain competencies differentiates High Performing and quick-to-settle down new hires from mediocre ones. The identified competencies are delivered though some of our various induction-oriented programmes:</p>

  <svg class="course-icon" viewBox="0 0 60 60" aria-hidden="true">
    <circle cx="27" cy="27" r="10" fill="none" stroke="#fff" stroke-width="3"/>
    <line x1="34" y1="34" x2="43" y2="43" stroke="#b6d07f" stroke-width="5" stroke-linecap="round"/>
  </svg>
  <h3 class="course-label">Idea Charting<br>for Problem Solving<br>and Creativity</h3>
  <div class="course-text">
    <p>Today’s work environment demands improved efficiency and a more creative approach to thinking and problem solving. High performance individuals are exemplified by their mental agility, the capacity to maintain high levels of concentration – “presence of mind” – creativity and the adeptness to communicate ideas and information with impact.</p>
    <p>The Idea Chart is a globally recognised and the single most effective and versatile organising, thinking and creativity tool of our time. From planning tasks through to solving complex business challenges, Idea Charting is a core competence required to dramatically enhance effectiveness and efficiency at work.</p>
    <p>Used as an essential business productivity tool for representing information and ideas in a non-linear manner; it brings clarity, improves recall and aids prioritisation whilst dramatically improving intelligence, creativity, communication, concentration, and memory.</p>
    <p>This <em>“Idea Charting for Problem Solving and Creativity”</em> is a global certification course facilitated by experienced ClearThink Licensed Instructors.</p>
  </div>

  <footer>
    <div class="brand"><span class="brand-name">quenlith</span><span class="brand-mark"></span></div>
    <span class="brand-parent">by Brightmere Group</span>
    <div class="page-number">3</div>
  </footer>
</body>
</html>
```